Business cards, stationery and report cover
For market research and marketing company in New Zealand
Simple
Rosalind Thorpe
Level 1
57 Pemberly Road
Milford
Auckland
PO Box 46-582
Auckland 0963
rosalind@lumenvex.co.nz
www.lumenvex.co.nz
From this process we are looking for business cards, letterhead, comp slip, as well as a generic cover page and inside page for our reports (e.g heading styles, footers etc). Both report pages need to be easily replicated or applied to Microsoft Word reports. We are PC users if this makes a difference.
The information for the business cards can be on the front or the back - depending on your design and what looks best. Most people would contact us by phone/cell/email.
We would like to be viewed as professional, competent, modern and well established. We don't want to look like we are an advertising agency, or quirky or too different from our competitors. However, we'd like to be eye catching and interesting! Our typical clients are intelligent managers who are over 35 years and a mixture of male and female.
Please let us know if you have any questions or would like clarification on anything.
As noted in 'Additional Comments' you can choose what details would look best on the front of the business card, and which you would recommend going on the back of the card.
This is our new logo.

```html
<!DOCTYPE html>
<html lang="en">
<head>
<meta charset="utf-8">
<title>Lumenvex stationery</title>
<link rel="stylesheet" href="https://fonts.googleapis.com/css2?family=Open+Sans:wght@400;600;700&display=swap">
<style>
  :root {
    --backdrop: #1c1c1e;
    --paper: #ffffff;
    --brand-blue: #3b78c9;
    --brand-blue-dark: #2a5fa8;
    --brand-blue-pale: #dfe9f6;
    --ink: #4a4f57;
    --ink-soft: #8a9099;
  }
  * { margin: 0; padding: 0; box-sizing: border-box; }
  html, body { width: 1200px; height: 617px; overflow: hidden; }
  body {
    background: var(--backdrop);
    font-family: "Open Sans", sans-serif;
    color: var(--ink);
    position: relative;
  }
  .sheet, .card { position: absolute; background: var(--paper); overflow: hidden; }

  .brand-name {
    font-family: "Open Sans", sans-serif;
    font-weight: 600;
    color: var(--brand-blue);
    letter-spacing: 0.5px;
    line-height: 1;
    display: flex; align-items: center; gap: 4px;
  }
  .brand-name .brand-dot {
    width: 0.45em; height: 0.45em; border-radius: 50%;
    background: var(--brand-blue);
  }

  /* Business card front */
  .card-front { left: 79px; top: 202px; width: 175px; height: 94px; border-radius: 6px; }
  .card-front .brand-name { position: absolute; left: 12px; top: 14px; font-size: 15px; }
  .card-front .holder { position: absolute; right: 12px; top: 15px; text-align: right; }
  .card-front .holder-name { font-size: 6px; font-weight: 700; color: var(--brand-blue); }
  .card-front .holder-role { font-size: 4.5px; color: var(--ink-soft); }
  .card-front .card-rule { position: absolute; left: 12px; right: 12px; top: 38px; height: 1px; background: #d7dbe0; }
  .card-front .card-details {
    position: absolute; left: 12px; right: 12px; top: 50px;
    display: flex; justify-content: space-between;
    font-size: 4.3px; line-height: 1.5; color: var(--ink);
  }

  /* Business card back */
  .card-back {
    left: 79px; top: 314px; width: 175px; height: 94px; border-radius: 6px;
    background: linear-gradient(180deg, #4584d3, var(--brand-blue-dark));
  }
  .card-back .brand-name { position: absolute; left: 0; right: 0; top: 32px; justify-content: center; color: #fff; font-size: 15px; }
  .card-back .brand-name .brand-dot { background: #fff; }
  .card-back .card-web { position: absolute; left: 0; right: 0; top: 60px; text-align: center; font-size: 4.5px; color: #e3ecf8; letter-spacing: 0.4px; }

  /* Letterhead */
  .letterhead { left: 278px; top: 48px; width: 404px; height: 521px; }
  .letterhead .brand-name { position: absolute; right: 22px; top: 26px; font-size: 22px; }
  .letterhead-footer {
    position: absolute; left: 14px; right: 14px; bottom: 16px;
    display: flex; gap: 62px;
    font-size: 4.5px; line-height: 1.55; color: var(--ink-soft);
  }
  .letterhead-footer .footer-col { padding-left: 6px; border-left: 1px solid #dfe2e6; }
  .letterhead-band {
    position: absolute; left: 0; right: 0; bottom: 0; height: 8px;
    background: var(--brand-blue);
    color: #fff; font-size: 4px; text-align: center; line-height: 8px; letter-spacing: 0.4px;
  }

  /* Report cover */
  .report-cover { left: 703px; top: 48px; width: 403px; height: 521px; }
  .cover-graphic { position: absolute; left: 0; right: 0; }
  .cover-graphic-top {
    top: 0; height: 22px;
    background: linear-gradient(180deg, var(--brand-blue) 0%, var(--brand-blue-pale) 100%);
  }
  .cover-graphic-bottom {
    bottom: 0; height: 110px;
    background: linear-gradient(180deg, var(--paper) 0%, var(--brand-blue-pale) 40%, var(--brand-blue) 100%);
  }
  .report-cover .brand-name { position: absolute; right: 30px; top: 36px; font-size: 20px; }
  .report-date { position: absolute; right: 14px; top: 86px; font-size: 4.5px; color: var(--ink-soft); }
  .report-title { position: absolute; left: 29px; top: 91px; font-size: 6.5px; font-weight: 700; color: var(--brand-blue); letter-spacing: 0.3px; }
  .report-client { position: absolute; left: 29px; top: 117px; font-size: 5.5px; font-weight: 600; color: var(--ink); letter-spacing: 0.3px; }
</style>
</head>
<body>

  <section class="card card-front">
    <div class="brand-name">lumenvex<span class="brand-dot"></span></div>
    <div class="holder">
      <div class="holder-name">Rosalind Thorpe</div>
      <div class="holder-role">Research Director</div>
    </div>
    <div class="card-rule"></div>
    <div class="card-details">
      <div>Level 1<br>57 Pemberly Road<br>Milford, Auckland</div>
      <div>PO Box 46-582<br>Auckland 0963</div>
      <div>M 021 555 0178<br>P 09 555 0142<br>rosalind@lumenvex.co.nz</div>
    </div>
  </section>

  <section class="card card-back">
    <div class="brand-name">lumenvex<span class="brand-dot"></span></div>
    <div class="card-web">www.lumenvex.co.nz</div>
  </section>

  <section class="sheet letterhead">
    <div class="brand-name">lumenvex<span class="brand-dot"></span></div>
    <div class="letterhead-footer">
      <div class="footer-col">Level 1<br>57 Pemberly Road<br>Milford, Auckland</div>
      <div class="footer-col">PO Box 46-582<br>Auckland 0963</div>
      <div class="footer-col">P 09 555 0142<br>F 09 555 0143<br>rosalind@lumenvex.co.nz</div>
    </div>
    <div class="letterhead-band">www.lumenvex.co.nz</div>
  </section>

  <section class="sheet report-cover">
    <div class="cover-graphic cover-graphic-top" role="img" aria-label="Blue decorative header wave"></div>
    <div class="brand-name">lumenvex<span class="brand-dot"></span></div>
    <div class="report-date">March 2012</div>
    <div class="report-title">BRAND RESEARCH RESULTS</div>
    <div class="report-client">ABC COMPANY</div>
    <div class="cover-graphic cover-graphic-bottom" role="img" aria-label="Blue and grey decorative footer wave"></div>
  </section>

</body>
</html>
```